Hardcore nerd needs to stand out in a sea of dull Defence business cards

Wombat Devices is a new Australian consulting engineering company that turns research and theory into practical systems. No evangelistic fluff, just mathematics and physics into electronic and optical circuits for consumer products, scientific research or Defence applications.

We already have a recognised logo (provided) which is often dark blue/black on a light background but we're open to other combinations. (Us engineers tend to have limited aesthetic imagination :)

Some of our recent products have included:
* Instrumentation for electrical testing,
* Radar jammers,
* GPS antenna design,
* Satellite tracking systems,
* High power lasers

We're open to both single and double-sided designs - happy to be convinced either way.

P.S. Another group is working on the web page, so - alas - our web site is currently of no use for images/ideas...

Target Market(s)

Engineering managers,
Scientists

Contact Information for Business Card

Dr Colin Marsh
R&D Engineer

colin@wombatdevicesco.com.au
0427 563 210

PO Box XXX (to be confirmed)
Banks ACT 2913
Australia

Font styles to use
Serif
Sans Serif

Colors

Designer to choose colors to be used in the design.

Requirements
Must have
• My contact details!
• I've had many (great) "bold and plain" designs submitted already, so feel free to be artistically creative :)
• Happy to take advice re fonts/colours/printability etc.
Nice to have
• I'm not sure if "lists" are more at home on a CV than a business card, but representative services include:
• Applied electromagnetics
• RF and high speed electronics
• Signal and image processing
• Electro-optical and laser systems
• Concept-to-prototype design services
• If you're considering double sided cards, then often measuring/alignment grids/rulers feature on the back of similar cards.
• e.g. https://www.lumoptix-example.com/newgrouppage9.cfm?objectgroup_id=4815
• https://www.lumoptix-example.com/newgrouppage9.cfm?objectgroup_ID=4817
• ..or even a "Smith chart" (google will return lots)
• Generic images to represent a capability might work - googling images associated with keyword for each of these areas might help:
• - "passive radar", "phased array", "fdtd", "vircator"
• RF and high speed electronic design
• - "smith chart", "microstrip circuits", "dimensioned drawing", "electronic schematic"
• - "dft", "iir filter"
• - "optical cavity". "laser energy level diagram"
• Background/watermarked images outlines/wireframes/schematics would probably look OK.
Should not have
• If a list of projects/services is provided, it is important not to make the client feel that this is "all" the company can do. Engineering design is a creative discipline (like graphics :)
• Please, no stock "military" snaps like planes, missiles, etc!

```html
<!DOCTYPE html>
<html lang="en">
<head>
<meta charset="utf-8">
<title>Wombat Devices – Business Card</title>
<link rel="stylesheet" href="https://fonts.googleapis.com/css2?family=Montserrat:wght@500;700;800&display=swap">
<style>
  :root {
    --navy: #1d2660;
    --paper: #f3f3f1;
    --stage: #6a6a6a;
    --faint: rgba(255, 255, 255, 0.08);
  }
  * { margin: 0; padding: 0; box-sizing: border-box; }
  html, body { width: 1200px; height: 911px; overflow: hidden; }
  body {
    background: var(--stage);
    font-family: "Montserrat", sans-serif;
    position: relative;
  }
  .card {
    position: absolute;
    left: 280px;
    width: 640px;
    height: 366px;
    overflow: hidden;
    border-radius: 2px;
  }
  .card--back { top: 62px; background: var(--navy); }
  .card--front { top: 480px; background: var(--paper); color: var(--navy); }

  .brand {
    position: absolute;
    display: flex;
    align-items: center;
    gap: 14px;
    font-weight: 800;
    letter-spacing: 0.04em;
    text-transform: uppercase;
    white-space: nowrap;
  }
  .brand__dot { border-radius: 50%; flex: none; }
  .card--back .brand { left: 92px; top: 150px; font-size: 30px; color: #fff; }
  .card--back .brand__dot { width: 58px; height: 58px; background: #fff; }
  .card--front .brand { left: 62px; top: 64px; font-size: 22px; color: var(--navy); }
  .card--front .brand__dot { width: 44px; height: 44px; background: var(--navy); }

  .backdrop-circle {
    position: absolute;
    border-radius: 50%;
  }
  .card--back .backdrop-circle {
    left: 330px; top: -110px; width: 420px; height: 420px;
    background: var(--faint);
  }
  .card--front .backdrop-circle {
    left: 332px; top: -60px; width: 460px; height: 460px;
    background: var(--navy);
  }

  .contact {
    position: absolute;
    left: 64px;
    top: 196px;
  }
  .contact__name { font-size: 22px; font-weight: 800; letter-spacing: 0.02em; text-transform: uppercase; line-height: 1.1; }
  .contact__role { font-size: 14px; font-weight: 500; margin-top: 2px; }
  .contact__rule { width: 20px; height: 2px; background: var(--navy); margin: 12px 0 10px; }
  .contact__address { font-size: 13px; font-weight: 500; line-height: 1.35; font-style: normal; }
  .contact__line {
    display: flex; align-items: center; gap: 8px;
    font-size: 13.5px; font-weight: 500; margin-top: 6px;
  }
  .contact__line:first-of-type { margin-top: 10px; }
  .contact__icon { width: 13px; height: 13px; flex: none; fill: var(--navy); }
</style>
</head>
<body>

<section class="card card--back" aria-label="Card back">
  <div class="backdrop-circle"></div>
  <div class="brand"><span class="brand__dot"></span>Wombat Devices</div>
</section>

<section class="card card--front" aria-label="Card front">
  <div class="backdrop-circle"></div>
  <div class="brand"><span class="brand__dot"></span>Wombat Devices</div>

  <div class="contact">
    <h1 class="contact__name">Dr Colin Marsh</h1>
    <p class="contact__role">R&amp;D Engineer</p>
    <div class="contact__rule"></div>
    <address class="contact__address">PO Box XXX<br>Banks ACT 2913, Australia</address>
    <p class="contact__line">
      <svg class="contact__icon" viewBox="0 0 24 24" aria-hidden="true"><path d="M6.6 10.8a15.1 15.1 0 0 0 6.6 6.6l2.2-2.2a1 1 0 0 1 1-.25 11.4 11.4 0 0 0 3.6.57 1 1 0 0 1 1 1V20a1 1 0 0 1-1 1A17 17 0 0 1 3 4a1 1 0 0 1 1-1h3.5a1 1 0 0 1 1 1c0 1.25.2 2.45.57 3.57a1 1 0 0 1-.25 1z"/></svg>
      0427 563 210
    </p>
    <p class="contact__line">
      <svg class="contact__icon" viewBox="0 0 24 24" aria-hidden="true"><path d="M2 5h20v14H2z M3.5 6.5 12 13l8.5-6.5" fill="none" stroke="#1d2660" stroke-width="2"/></svg>
      colin@wombatdevicesco.com.au
    </p>
  </div>
</section>

</body>
</html>
```